Dynamic Book Cover Design
Lines That Hold
Creative Brief
ABOUT THE PROJECT "Lines That Hold: Seven Notes from a Counselor" is a practical, warm, and deeply insightful self-help ebook written by a licensed therapist (Morgan Pellow, LPC). Unlike generic self-help books that treat boundaries like a list of aggressive demands you make on other people, this book flips the script. The core concept is that a true boundary is an internal decision about yourself. One that holds firm no matter how the other person reacts. It is about self-possession, peace, and clarity. The book will be featured on my private practice website and on Quillmart. The cover needs to instantly communicate trust, professional clinical authority, and approachable warmth. I want it to look like a book you would see prominently displayed in a high-end wellness boutique or a psychology section, rather than a loud, busy, or flashy paperback. THE DESIGN DIRECTION Style: Clean, modern, uncluttered, and grounded. Tone: Firm but kind. Calm rather than aggressive. Typography: The title needs to be highly legible and crisp, even at thumbnail size on Quillmart. Thank you so much for your time and creativity. I can't wait to see how you bring this concept to life!
Health
Adults who feel drained, over-committed, or taken advantage of, and who struggle to say no or hold a limit. Broad appeal, leaning slightly female but not exclusively. These are thoughtful readers, not looking for hype. The cover should feel calm, credible, and reassuring, like something a good therapist would hand you. But still interesting to look at.
CREATIVE FREEDOM & METAPHORS I am entirely open to your creative interpretation! If you want to use a visual metaphor for a "boundary", please do. However, I want to completely steer clear of cliché, heavy-handed imagery. Please AVOID: • Brick walls, fences, barbed wire, or stop signs. • "No" symbols or literal hands pushing someone away. • Harsh reds or alarm-style, anxiety-inducing imagery. • Cheesy, dated stock photos. • Anything that feels cold, sterile, or overly clinical. BRANDING & COLORS This book is an extension of my therapy practice, so the cover design must feel cohesive with my existing brand. Please visit my website at https://morganpellowcounsel.example to view my current color palette, aesthetic, and font family (Montserrat). I want the book to feel like it naturally belongs in that digital space. DELIVERABLES REQUIRED • Front Ebook Cover (optimized for digital/Quillmart) • Full wrap layout including a spine and back cover (for potential future print runs)

```html
<!DOCTYPE html>
<html lang="en">
<head>
<meta charset="utf-8">
<title>Lines That Hold – Full Wrap Cover</title>
<link href="https://fonts.googleapis.com/css2?family=Cormorant+Garamond:wght@500;600;700&family=Montserrat:wght@400;500;600;700&family=Allura&display=swap" rel="stylesheet">
<style>
  :root{
    --cream:#f4f0e7;
    --cream-deep:#ebe5d8;
    --forest:#3e5040;
    --forest-dark:#2f3d31;
    --sage:#8c9b84;
    --ink:#3a3f38;
    --muted:#6b6f66;
    --line:#cfc8b6;
    --mist-top:#d9dbd2;
    --mist-mid:#a7ad9c;
    --mist-low:#5f6a58;
  }
  *{box-sizing:border-box;margin:0;padding:0}
  html,body{width:1200px;height:799px;overflow:hidden;background:var(--cream)}
  .wrap{position:relative;width:1200px;height:799px;display:flex;font-family:"Montserrat",sans-serif;color:var(--ink)}

  /* Back cover */
  .back{width:552px;height:799px;background:var(--cream);padding:26px 30px 0 26px;position:relative}
  .back-headline{font-family:"Cormorant Garamond",serif;font-weight:600;font-size:19px;line-height:1.35;color:var(--forest-dark)}
  .back-headline em{font-style:italic;color:var(--forest)}
  .back-copy{font-size:10.5px;line-height:1.6;margin-top:14px;color:var(--ink)}
  .back-copy strong{font-weight:700;color:var(--forest-dark)}
  .back-copy + .back-copy{margin-top:8px}
  .discover{margin-top:16px;border:1px solid var(--line);background:var(--cream-deep);padding:12px 14px 14px;border-radius:3px}
  .discover-title{font-size:9.5px;font-weight:700;letter-spacing:.08em;color:var(--forest);text-align:center}
  .discover-grid{display:grid;grid-template-columns:repeat(3,1fr);gap:12px 10px;margin-top:12px}
  .rule{text-align:center;font-size:9px;line-height:1.35;color:var(--ink)}
  .rule svg{display:block;margin:0 auto 5px;width:28px;height:28px}
  .closing{font-size:10.5px;line-height:1.6;margin-top:16px}
  .author-block{display:flex;gap:14px;margin-top:18px;align-items:flex-start}
  .author-photo{width:118px;height:122px;flex:none;background:linear-gradient(160deg,#8d9886,#5a6553);border-radius:2px}
  .author-bio{font-size:9.5px;line-height:1.55;max-width:250px}
  .author-bio h3{font-size:11px;font-weight:700;letter-spacing:.06em;color:var(--forest-dark);margin-bottom:4px}
  .practice{position:absolute;left:26px;bottom:24px;display:flex;align-items:center;gap:8px;font-size:10px;font-weight:600;letter-spacing:.12em;color:var(--forest)}
  .practice .mark{width:18px;height:18px;border:1.5px solid var(--forest)}

  /* Spine */
  .spine{width:84px;height:799px;background:var(--forest);position:relative;color:var(--cream)}
  .spine-text{position:absolute;left:50%;top:50%;transform:translate(-50%,-50%) rotate(90deg);white-space:nowrap;display:flex;align-items:center;gap:40px}
  .spine-title{font-family:"Cormorant Garamond",serif;font-weight:600;font-size:34px;letter-spacing:.12em}
  .spine-author{font-size:13px;font-weight:500;letter-spacing:.16em}
  .spine-mark{position:absolute;left:50%;bottom:28px;width:22px;height:22px;margin-left:-11px;border:1.5px solid var(--cream)}

  /* Front cover */
  .front{flex:1;height:799px;position:relative;background:var(--cream);overflow:hidden}
  .scene{position:absolute;left:0;right:0;bottom:0;height:460px;background:linear-gradient(180deg,var(--cream) 0%,var(--mist-top) 14%,var(--mist-mid) 48%,var(--mist-low) 100%)}
  .front-kicker{position:absolute;top:28px;width:100%;text-align:center;font-size:13px;font-weight:600;letter-spacing:.22em;color:var(--forest)}
  .front-title{position:absolute;top:58px;width:100%;text-align:center;font-family:"Cormorant Garamond",serif;font-weight:600;color:var(--forest-dark);line-height:1}
  .front-title .t1{display:block;font-size:92px;letter-spacing:.02em}
  .front-title .t2{display:block;font-size:52px;letter-spacing:.04em;margin-top:6px}
  .front-title .script{font-family:"Allura",cursive;font-size:76px;letter-spacing:0;font-weight:400}
  .divider{position:absolute;top:262px;left:50%;transform:translateX(-50%)}
  .front-sub{position:absolute;top:292px;left:60px;right:60px;text-align:center;font-family:"Cormorant Garamond",serif;font-size:21px;font-weight:500;line-height:1.3;color:var(--forest-dark)}
  .badge{position:absolute;right:24px;top:450px;width:118px;height:118px;border-radius:50%;background:rgba(244,240,231,.85);display:flex;flex-direction:column;align-items:center;justify-content:center;text-align:center;font-size:9px;font-weight:700;letter-spacing:.1em;line-height:1.5;color:var(--forest)}
  .badge small{font-weight:400;font-size:8px;letter-spacing:.04em}
  .front-author{position:absolute;bottom:44px;width:100%;text-align:center;font-family:"Cormorant Garamond",serif;font-weight:600;font-size:34px;letter-spacing:.12em;color:var(--cream)}
  .front-role{position:absolute;bottom:20px;width:100%;text-align:center;font-size:11px;font-weight:500;letter-spacing:.28em;color:var(--cream)}
  .front-practice{position:absolute;right:22px;bottom:20px;font-size:9px;font-weight:600;letter-spacing:.08em;color:var(--cream)}
</style>
</head>
<body>
<div class="wrap">

  <section class="back">
    <h2 class="back-headline">Lines aren’t about controlling others.<br>They’re about honoring <em>yourself.</em></h2>
    <p class="back-copy">If you often feel overwhelmed, over-committed, or taken for granted, you’re not alone—and you’re not powerless.</p>
    <p class="back-copy"><strong>Lines That Hold</strong> offers a fresh, therapist-approved approach to one of life’s most important skills. This book will help you stop abandoning yourself to keep the peace and start making decisions that protect your time, energy, and well-being.</p>

    <div class="discover">
      <p class="discover-title">INSIDE, YOU’LL DISCOVER SIX PRACTICAL RULES TO HELP YOU:</p>
      <div class="discover-grid">
        <div class="rule"><svg viewBox="0 0 28 28" fill="none" stroke="#3e5040" stroke-width="1.4"><circle cx="14" cy="14" r="11"/><path d="M9 14l3.5 3.5L19 11"/></svg>Understand what boundaries really are (and aren’t)</div>
        <div class="rule"><svg viewBox="0 0 28 28" fill="none" stroke="#3e5040" stroke-width="1.4"><circle cx="14" cy="14" r="11"/><path d="M8 14h12"/></svg>Set clear limits without guilt</div>
        <div class="rule"><svg viewBox="0 0 28 28" fill="none" stroke="#3e5040" stroke-width="1.4"><circle cx="14" cy="16" r="5"/><path d="M14 5v3M5 16h3M20 16h3M7.5 9.5l2 2M20.5 9.5l-2 2"/></svg>Stay grounded no matter how others respond</div>
        <div class="rule"><svg viewBox="0 0 28 28" fill="none" stroke="#3e5040" stroke-width="1.4"><path d="M6 22L22 6M6 6l6 6M16 16l6 6"/></svg>Break old patterns and people-pleasing habits</div>
        <div class="rule"><svg viewBox="0 0 28 28" fill="none" stroke="#3e5040" stroke-width="1.4"><path d="M14 23s-9-5.5-9-11.5A4.5 4.5 0 0 1 14 9a4.5 4.5 0 0 1 9 2.5C23 17.5 14 23 14 23z"/></svg>Build relationships based on respect, not rescue</div>
        <div class="rule"><svg viewBox="0 0 28 28" fill="none" stroke="#3e5040" stroke-width="1.4"><path d="M14 24V6M14 12l-5-4M14 12l5-4M14 18l-6-4M14 18l6-4"/></svg>Live with more clarity, confidence, and inner peace</div>
      </div>
    </div>

    <p class="closing">Warm, wise, and deeply practical, this book is like a conversation with a therapist who truly gets it—and who can help you create boundaries that actually work in real life.</p>

    <div class="author-block">
      <div class="author-photo" role="img" aria-label="Author portrait photograph"></div>
      <div class="author-bio">
        <h3>MORGAN PELLOW, LPC</h3>
        <p>is a licensed therapist with a passion for helping individuals build healthier relationships, cultivate self-trust, and create a life that feels aligned and meaningful.</p>
        <p>Learn more at morganpellowcounsel.example</p>
      </div>
    </div>

    <div class="practice"><span class="mark"></span>MORGAN PELLOW COUNSEL</div>
  </section>

  <section class="spine">
    <div class="spine-text">
      <span class="spine-title">LINES THAT HOLD</span>
      <span class="spine-author">MORGAN PELLOW, LPC</span>
    </div>
    <span class="spine-mark"></span>
  </section>

  <section class="front">
    <div class="scene" role="img" aria-label="Photograph of a person seated on a rock looking out over a calm misty lake and hills"></div>
    <p class="front-kicker">SEVEN NOTES FROM A COUNSELOR</p>
    <h1 class="front-title">
      <span class="t1">LINES</span>
      <span class="t2">THAT <span class="script">Hold</span></span>
    </h1>
    <svg class="divider" width="160" height="16" viewBox="0 0 160 16" fill="none" stroke="#3e5040" stroke-width="1">
      <path d="M0 8h62M98 8h62"/>
      <circle cx="80" cy="8" r="4"/>
    </svg>
    <p class="front-sub">A Practical Guide to Protecting Your Peace, Staying True to Yourself, and Building Healthier Relationships</p>
    <div class="badge">CLARITY.<br>CONFIDENCE.<br>CONNECTION.<small>one calm step</small></div>
    <p class="front-author">MORGAN PELLOW, LPC</p>
    <p class="front-role">LICENSED THERAPIST</p>
  </section>

</div>
</body>
</html>
```